Realtor needs 8 1/2 x 11 flyer designed both sides

I uploaded a new word doc to be used under each of the pictures on the front page.

Colors

Designer to choose colors to be used in the design.

```html
<!DOCTYPE html>
<html lang="en">
<head>
<meta charset="utf-8">
<title>Laura Bellamy Realtor Flyer</title>
<link href="https://fonts.googleapis.com/css2?family=Tinos:wght@700&family=Lato:ital,wght@0,400;0,700;1,400&family=Arimo:wght@400;700&display=swap" rel="stylesheet">
<style>
:root{
  --blue:#3560b8;
  --blue-dark:#294a9c;
  --blue-text:#2f5cb3;
  --paper:#f4f5f7;
  --ink:#1c1c1c;
  --grey-text:#555;
  --backdrop:#e4e4e4;
}
*{margin:0;padding:0;box-sizing:border-box}
html,body{width:1200px;height:771px;overflow:hidden;background:var(--backdrop)}
.canvas{position:relative;width:1200px;height:771px}
.page{position:absolute;top:52px;width:613px;height:792px;transform:scale(.829);transform-origin:0 0;background:var(--paper);overflow:hidden;font-family:"Lato",sans-serif;color:var(--ink)}
.page--inside{left:64px}
.page--cover{left:622px;background:var(--blue)}
.page-shapes{position:absolute;inset:0;width:613px;height:792px}
.abs{position:absolute}
.headline{left:18px;top:30px;font-family:"Tinos",serif;font-weight:700;font-size:45px;line-height:44px;color:#fff;letter-spacing:.5px}
.portrait-frame{width:94px;height:93px;border:1px solid #c9c9c9;background:#fff;padding:3px}
.portrait-frame div{width:100%;height:100%}
.agent-meta{font-size:11px;line-height:15px;color:var(--grey-text)}
.agent-meta small{display:block;font-size:7.5px;line-height:10px}
.note-title{font-size:16.5px;color:var(--blue-text);letter-spacing:-.2px}
.note-body{width:277px;font-size:9.4px;line-height:10.9px;letter-spacing:-.15px;text-align:justify}
.note-body p{margin-bottom:11px}
.contact{color:#fff;font-size:10px}
.contact h3{font-size:13.5px;font-weight:700;letter-spacing:.2px;margin-bottom:12px}
.contact li{list-style:none;display:flex;align-items:center;gap:6px;height:17px}
.contact--right{text-align:right}
.contact--right li{justify-content:flex-end}
.icon{width:12px;height:12px;flex:none}
.brand-lockup{left:205px;top:420px;display:flex;align-items:center;gap:10px;color:var(--blue-text);font-size:30px;font-weight:700;letter-spacing:.5px}
.brand-lockup span.mark{width:18px;height:18px;background:#c9ccd3}
.brand-role{left:295px;top:458px;font-size:8px;letter-spacing:1px;color:#333}
.cover-meta{left:196px;top:523px;font-size:14px;line-height:19px;color:var(--grey-text)}
.cover-meta small{display:block;font-size:10px;line-height:18px}
.cover-message{left:196px;top:586px;width:175px;font-style:italic;font-size:14px;line-height:16px;color:#222}
.postal-box{border:1px solid #666;background:#fff;font-family:"Arimo",sans-serif;color:#111}
.permit{left:510px;top:449px;width:86px;height:85px;font-size:11.5px;line-height:13.5px;text-align:center;padding-top:5px}
.address{left:383px;top:563px;width:213px;height:86px;font-size:12.5px;line-height:14px;padding:10px 14px}
.address .route{font-size:10px;text-align:right;margin-bottom:16px}
.office{right:20px;bottom:40px;display:flex;align-items:center;gap:6px;color:#fff;font-weight:700;font-size:12px}
.office span.dot{width:14px;height:14px;border-radius:50%;background:#fff}
</style>
</head>
<body>
<div class="canvas">

  <section class="page page--inside">
    <svg class="page-shapes" viewBox="0 0 613 792">
      <defs>
        <linearGradient id="poolScene" x1="0" y1="0" x2="0" y2="1">
          <stop offset="0" stop-color="#7f88a8"/><stop offset=".55" stop-color="#6b5a52"/><stop offset="1" stop-color="#1e2a44"/>
        </linearGradient>
      </defs>
      <polygon points="0,0 613,0 613,205 540,268 0,195" fill="url(#poolScene)" role="img" aria-label="Photo of a modern home with a lit pool terrace at dusk"/>
      <polygon points="613,200 613,268 400,268" fill="var(--blue)"/>
      <polygon points="0,648 263,722 613,792 0,792" fill="var(--blue)"/>
      <polygon points="263,722 613,659 613,792 330,792" fill="var(--blue-dark)"/>
    </svg>

    <h1 class="abs headline">WHY<br>CHOSE US?</h1>

    <div class="abs portrait-frame" style="left:17px;top:277px"><div style="background:linear-gradient(#d8cfc4,#b89a72)" role="img" aria-label="Portrait of Laura Bellamy"></div></div>
    <div class="abs agent-meta" style="left:121px;top:306px">Laura Bellamy<br>Realtor ®<small>DRE# 01234567</small></div>
    <h2 class="abs note-title" style="left:121px;top:354px">A NOTE FROM LAURA</h2>
    <div class="abs note-body" style="left:17px;top:383px">
      <p>I Know many of you, but for those whom I do not, I'd like to introduce myself. I've been a resident of Harbor Crest for almost 23 years now. I've loved our neighborhood from the first time I discovered it. From our beautiful parks to our fabulous pool and amenities, it's hard to beat our wonderful community.</p>
      <p>I always say where we live is the next best thing to living on a tropical island. I've traveled to many and I'm always happy to come back to my Harbor Crest home. My passion for this area is why I'm in Real Estate. I consider myself incredibly fortunate to sell homes and help people purchase homes in an area that I love with all my heart.</p>
      <p>Marta and I have been close colleagues for the last 8 years, both working as Realtors and long time residents of Harbor Crest. I am most grateful for our working relationship and the friendship we have formed. I am humbled by her trust and respect for me.</p>
      <p>Please feel welcome to call on me for all things home-related. I will look forward to meeting you!</p>
    </div>

    <div class="abs portrait-frame" style="left:318px;top:277px"><div style="background:linear-gradient(#e6e2dc,#c9b28a)" role="img" aria-label="Portrait of Marta Sloane"></div></div>
    <div class="abs agent-meta" style="left:422px;top:306px">Marta Sloane<br>Realtor ®<small>DRE# 00765432</small></div>
    <h2 class="abs note-title" style="left:422px;top:354px">A NOTE FROM MARTA</h2>
    <div class="abs note-body" style="left:317px;top:383px">
      <p>I have exciting and bittersweet news I want to share with my Harbor Crest clients, friends and neighbors. After 40 (some-thing) years in the Real Estate business, I have decided to retire. Some of you may know last month I sold my Harbor Crest home and moved to the beautiful Cedar Glen community in Rancho Alder Vista.</p>
      <p>My husband and I wanted to scale down and have time to enjoy retirement, together. I have been so blessed to have had an illustrious career in Real Estate and I want to thank you with a most grateful heart for giving me the opportunity to work with you. I have enjoyed every minute. I'm happy and proud to be turning my business over to Laura Bellamy, fellow Summit agent. She and I have enjoyed a very close working relationship for many years and there is nobody else except Laura I'd consider turning my business over to. Laura is....I will add verbiage here conveying your thoughts about me. Please contact me if you'd like a personal introduction to Laura or contact her directly.</p>
      <p>Remember to mention me when you contact Laura and let her know that we know each other. I wish you the very best and please say hello when you see me in the neighborhood.</p>
    </div>

    <div class="abs contact" style="left:17px;top:703px">
      <h3>LAURA BELLAMY</h3>
      <ul>
        <li><svg class="icon" viewBox="0 0 12 12"><circle cx="6" cy="6" r="5.4" fill="none" stroke="#fff"/><path d="M4 3.2l1 1.2-.6.8c.4.9 1 1.5 1.9 1.9l.8-.6 1.2 1-.7 1C5.5 8.3 3.7 6.5 3.3 4z" fill="#fff"/></svg>555 214 3087</li>
        <li><svg class="icon" viewBox="0 0 12 12"><circle cx="6" cy="6" r="5.4" fill="none" stroke="#fff"/><rect x="3" y="4" width="6" height="4" fill="#fff"/><path d="M3 4l3 2 3-2" stroke="var(--blue)" stroke-width=".7" fill="none"/></svg>laura@laurabhomes.com</li>
        <li><svg class="icon" viewBox="0 0 12 12"><circle cx="6" cy="6" r="5.4" fill="none" stroke="#fff"/><circle cx="6" cy="6" r="3.2" fill="none" stroke="#fff" stroke-width=".7"/><path d="M2.8 6h6.4M6 2.8v6.4" stroke="#fff" stroke-width=".7"/></svg>www.laurabhomes.com</li>
      </ul>
    </div>
    <div class="abs contact contact--right" style="right:19px;top:703px">
      <h3>MARTA SLOANE</h3>
      <ul>
        <li>555 407 6621<svg class="icon" viewBox="0 0 12 12"><circle cx="6" cy="6" r="5.4" fill="none" stroke="#fff"/><path d="M4 3.2l1 1.2-.6.8c.4.9 1 1.5 1.9 1.9l.8-.6 1.2 1-.7 1C5.5 8.3 3.7 6.5 3.3 4z" fill="#fff"/></svg></li>
        <li>marta@martasloane.com<svg class="icon" viewBox="0 0 12 12"><circle cx="6" cy="6" r="5.4" fill="none" stroke="#fff"/><rect x="3" y="4" width="6" height="4" fill="#fff"/><path d="M3 4l3 2 3-2" stroke="var(--blue-dark)" stroke-width=".7" fill="none"/></svg></li>
        <li>www.martasloane.com<svg class="icon" viewBox="0 0 12 12"><circle cx="6" cy="6" r="5.4" fill="none" stroke="#fff"/><circle cx="6" cy="6" r="3.2" fill="none" stroke="#fff" stroke-width=".7"/><path d="M2.8 6h6.4M6 2.8v6.4" stroke="#fff" stroke-width=".7"/></svg></li>
      </ul>
    </div>
  </section>

  <section class="page page--cover">
    <svg class="page-shapes" viewBox="0 0 613 792">
      <defs>
        <linearGradient id="estateScene" x1="0" y1="0" x2="0" y2="1">
          <stop offset="0" stop-color="#1d3a78"/><stop offset=".45" stop-color="#a98a5e"/><stop offset="1" stop-color="#4d5a63"/>
        </linearGradient>
        <linearGradient id="coverPortrait" x1="0" y1="0" x2="0" y2="1">
          <stop offset="0" stop-color="#e2d3bb"/><stop offset=".6" stop-color="#c7a77a"/><stop offset="1" stop-color="#2a2a2e"/>
        </linearGradient>
      </defs>
      <polygon points="8,75 160,0 613,0 613,117 350,257 8,410" fill="url(#estateScene)" role="img" aria-label="Photo of a lit Mediterranean-style estate with palm trees at dusk"/>
      <polygon points="0,417 350,255 613,442 613,792 0,792" fill="var(--paper)"/>
      <rect x="10" y="422" width="170" height="226" fill="url(#coverPortrait)" role="img" aria-label="Portrait of Laura Bellamy"/>
      <polygon points="0,648 350,727 613,792 0,792" fill="var(--blue)"/>
      <polygon points="350,727 613,657 613,792 420,792" fill="var(--blue-dark)"/>
    </svg>

    <div class="abs brand-lockup"><span class="mark"></span>LAURA BELLAMY</div>
    <div class="abs brand-role">REALTOR®</div>

    <div class="abs cover-meta">Laura Bellamy<br>Realtor ®<small>DRE# 01234567</small></div>
    <p class="abs cover-message">Please feel welcome to call on me for all things home-related. I will look forward to meeting you!</p>

    <div class="abs postal-box permit">PRSRT STD<br>ECRWSS<br>U.S. Postage<br><b>PAID</b><br>EDDM RETAIL</div>
    <div class="abs postal-box address"><div class="route">****************ECRWSS****</div>Local<br>Postal Customer</div>

    <div class="abs contact" style="left:17px;top:703px">
      <h3>LAURA BELLAMY</h3>
      <ul>
        <li><svg class="icon" viewBox="0 0 12 12"><circle cx="6" cy="6" r="5.4" fill="none" stroke="#fff"/><path d="M4 3.2l1 1.2-.6.8c.4.9 1 1.5 1.9 1.9l.8-.6 1.2 1-.7 1C5.5 8.3 3.7 6.5 3.3 4z" fill="#fff"/></svg>555 214 3087</li>
        <li><svg class="icon" viewBox="0 0 12 12"><circle cx="6" cy="6" r="5.4" fill="none" stroke="#fff"/><rect x="3" y="4" width="6" height="4" fill="#fff"/><path d="M3 4l3 2 3-2" stroke="var(--blue)" stroke-width=".7" fill="none"/></svg>laura@laurabhomes.com</li>
        <li><svg class="icon" viewBox="0 0 12 12"><circle cx="6" cy="6" r="5.4" fill="none" stroke="#fff"/><circle cx="6" cy="6" r="3.2" fill="none" stroke="#fff" stroke-width=".7"/><path d="M2.8 6h6.4M6 2.8v6.4" stroke="#fff" stroke-width=".7"/></svg>www.laurabhomes.com</li>
      </ul>
    </div>
    <div class="abs office"><span class="dot"></span>Summit Realty</div>
  </section>

</div>
</body>
</html>
```